I want a double sided flyer possibly with a picture of a lawn or grass.
Company name, phone number, email, and logo
Halvorsen Turf Management, (404)726-1853,Halvorsen_Turf@brevimail.com
Company services
Fertilization and weed control,Lawn and Landscape maintenance, mowing, pruning, aeration, landscape and Christmas lights,

```html
<!DOCTYPE html>
<html lang="en">
<head>
<meta charset="utf-8">
<title>Halvorsen Turf Management – Company Services</title>
<link rel="stylesheet" href="https://fonts.googleapis.com/css2?family=Noto+Serif:wght@400;700&display=swap">
<style>
  :root {
    --navy: #0b2160;
    --lime: #8cc63f;
    --sage: #c5d99b;
    --earth: #4a4233;
    --ink: #4a3f2a;
    --white: #ffffff;
    --leaf: #5fae3a;
  }
  html, body {
    margin: 0;
    padding: 0;
    overflow: hidden;
    background: var(--white);
  }
  .flyer {
    position: relative;
    width: 927px;
    height: 1200px;
    background: var(--white);
    font-family: "Noto Serif", Georgia, serif;
    overflow: hidden;
  }
  .block { position: absolute; box-sizing: border-box; }

  .brand {
    left: 27px; top: 28px; width: 272px; height: 251px;
    background: var(--navy);
    display: flex; flex-direction: column;
    align-items: center; justify-content: center; gap: 14px;
  }
  .brand-dot {
    width: 54px; height: 54px; border-radius: 50%;
    background: var(--leaf);
  }
  .brand-name {
    margin: 0;
    color: var(--leaf);
    font-weight: 700;
    font-size: 28px;
    line-height: 1.15;
    text-align: center;
  }

  .headline {
    left: 328px; top: 28px; width: 572px; height: 251px;
    background: var(--lime);
    padding: 52px 0 0 24px;
  }
  .headline h1 {
    margin: 0;
    color: var(--ink);
    font-weight: 400;
    font-size: 68px;
    line-height: 66px;
  }

  .call-out {
    left: 29px; top: 303px; width: 272px; height: 436px;
    background: var(--sage);
    display: flex; align-items: center; justify-content: center;
  }
  .call-out p {
    margin: 0 0 18px;
    color: var(--ink);
    font-weight: 700;
    font-size: 45px;
    line-height: 71px;
    text-align: center;
  }

  .services {
    left: 328px; top: 305px; width: 572px; height: 436px;
    background: var(--earth);
  }
  .service-list {
    position: absolute; left: 52px; top: 70px;
    margin: 0; padding: 0 0 0 25px;
    color: var(--white);
    font-size: 23px;
    line-height: 33.5px;
    list-style: disc;
  }
  .plant-art {
    position: absolute; left: 360px; top: 20px; width: 210px; height: 416px;
    background: linear-gradient(180deg, #4a4233 0%, #3f8f32 35%, #4aa83a 60%, #b3241c 88%, #4a4233 100%);
    border-radius: 4px;
    opacity: 0.85;
  }

  .photo { top: 768px; height: 256px; }
  .photo-garden { left: 30px; width: 332px;
    background: linear-gradient(160deg, #e9efe4 0%, #4f7a35 35%, #2f5a25 70%, #8a8b6a 100%); }
  .photo-tools { left: 381px; width: 193px;
    background: linear-gradient(180deg, #d9d9d4 0%, #8a7a66 50%, #5e4c3d 100%); }
  .photo-mower { left: 593px; width: 307px;
    background: linear-gradient(150deg, #9a7a55 0%, #3b6b2a 45%, #7fb04a 100%); }

  .contact {
    left: 27px; top: 1062px; width: 873px; height: 109px;
    background: var(--lime);
    color: var(--white);
    text-align: center;
    padding-top: 22px;
    font-size: 21px;
    line-height: 25px;
  }
  .contact p { margin: 0; }
</style>
</head>
<body>
<main class="flyer">
  <header class="block brand">
    <span class="brand-dot" aria-hidden="true"></span>
    <p class="brand-name">Halvorsen<br>Turf Management</p>
  </header>

  <section class="block headline">
    <h1>Company<br>Services:</h1>
  </section>

  <section class="block call-out">
    <p>Don’t<br>hesitate,<br>call us!</p>
  </section>

  <section class="block services">
    <ul class="service-list">
      <li>Fertilization and<br>Weed Control</li>
      <li>Lawn and Landscape<br>Maintenance</li>
      <li>Mowing</li>
      <li>Pruning</li>
      <li>Aeration</li>
      <li>Landscape and<br>Christmas Lights</li>
    </ul>
    <div class="plant-art" role="img" aria-label="Illustration of a leafy young plant growing in a red pot"></div>
  </section>

  <div class="block photo photo-garden" role="img" aria-label="Photo of a lush landscaped garden with a stepping-stone path"></div>
  <div class="block photo photo-tools" role="img" aria-label="Photo of pruning shears, a saw and cut branches on a wooden pallet"></div>
  <div class="block photo photo-mower" role="img" aria-label="Photo of a reel mower cutting green grass"></div>

  <footer class="block contact">
    <p>Halvorsen Turf Management</p>
    <p>(404) 726-1853 ♦ Halvorsen_Turf@brevimail.com</p>
  </footer>
</main>
</body>
</html>
```